Homepage for the brisk-trail Web Application

At the end of this text, you will find a link to a website that is under construction for a webApp that I intend to launch soon. The contest goal is for you to make redesign the homepage in a nice, fresh, modern Style. Only design, no coding necessary. It needs to have a responsive version for small screens like smart phones. Attached is the text for it, and some images that you may use. You are welcome to find or create additional supporting images. You can use PixVaultimages.com or similar service to find new images as long as I can purchase the non-exclusive use rights for the images at similar prices. The contest is just for the home page. However, the winner, if I like the work and we can agree on a fair price, could be contracted on a one-on-one basis to do the rest of the site. You are welcome to suggest minor changes like font sizes and minor variations on the Header banner, but that banner is consistent with the user interface of the application therefore should not change too much. The information should flow somewhat continually without much use of side bars or things like that.
https://www.brisk-trail-example.com
Sincerely,
Marco R. Delgado

```html
<!DOCTYPE html>
<html lang="en">
<head>
<meta charset="utf-8">
<title>Brisk-Trail — Find that document or item instantly</title>
<link rel="stylesheet" href="https://fonts.googleapis.com/css2?family=Libre+Baskerville:wght@400;700&display=swap">
<style>
:root{
  --teal:#3dbfc9;
  --teal-dark:#2aa6b1;
  --teal-light:#bfeef1;
  --orange:#ff6e4a;
  --orange-light:#ff9a7d;
  --ink:#2d2d2d;
  --body:#444;
  --grey-bg:#f3f3f3;
  --white:#fff;
}
*{box-sizing:border-box;margin:0;padding:0}
html,body{width:1200px;height:4057px;overflow:hidden}
body{position:relative;background:var(--white);font-family:"Libre Baskerville",Georgia,serif;color:var(--ink)}
.abs{position:absolute}

/* header */
.brand{display:flex;align-items:center;gap:10px;font-size:30px;color:var(--orange);font-weight:400}
.brand-dot{width:34px;height:34px;border-radius:50%;border:3px solid var(--ink)}
.site-header .brand{left:106px;top:34px}
.main-nav a{position:absolute;top:48px;font-size:14px;font-weight:700;color:var(--ink);text-decoration:none}
.btn{display:inline-flex;align-items:center;justify-content:center;background:var(--orange);color:var(--white);border-radius:30px;font-size:12px;text-transform:uppercase;letter-spacing:.5px;box-shadow:0 6px 14px rgba(255,110,74,.35);text-decoration:none}
.btn-login{left:1000px;top:39px;width:94px;height:37px}

/* hero */
.hero-title{left:164px;top:214px;font-size:44px;line-height:52px;font-weight:700;color:var(--teal)}
.hero-title .dark{color:var(--ink)}
.hero-title .accent{color:var(--orange)}
.hero-text{left:164px;top:336px;width:420px;font-size:14.5px;line-height:21.5px;color:var(--body)}
.btn-more{left:160px;top:460px;width:152px;height:44px}
.art{border-radius:18px}
.hero-art{left:583px;top:102px;width:535px;height:552px;background:linear-gradient(150deg,var(--teal-light),var(--teal) 60%,var(--teal-dark));clip-path:polygon(24% 0,100% 18%,100% 70%,60% 100%,0 78%,10% 55%,24% 40%)}

/* teal section */
.waves{left:0;top:0;width:1200px;height:4057px}
.why-title{left:0;top:808px;width:1200px;text-align:center;font-size:46px;line-height:56px;color:var(--white);font-weight:700}
.paper-title{left:193px;top:1008px;font-size:37px;line-height:39px;color:var(--white);font-weight:700}
.paper-text{left:195px;top:1102px;width:510px;color:var(--white);font-size:14px;line-height:21.5px}
.paper-text p{margin-bottom:21.5px}
.phone-art{left:748px;top:1008px;width:237px;height:567px;background:linear-gradient(160deg,#d9f7f8,#8fdde2 55%,var(--teal-dark));border-radius:28px;clip-path:polygon(10% 0,100% 12%,100% 100%,0 88%)}

/* objects section */
.objects-title{left:0;top:1786px;width:1200px;text-align:center;font-size:34px;font-weight:700}
.objects-sub{left:0;top:1853px;width:1200px;text-align:center;font-size:15px;color:var(--body)}
.card{position:absolute;width:462px;height:158px;border:2px solid var(--teal);border-radius:80px;background:var(--white)}
.card .icon{position:absolute;top:6px;width:142px;height:142px;border-radius:50%;background:var(--white);box-shadow:0 6px 16px rgba(0,0,0,.18);display:flex;align-items:center;justify-content:center}
.card .ring{position:absolute;top:-8px;width:172px;height:172px;border-radius:50%;border:12px solid var(--teal)}
.card-left .ring{right:-26px;border-left-color:transparent;border-bottom-color:transparent;transform:rotate(45deg)}
.card-right .ring{left:-26px;border-right-color:transparent;border-top-color:transparent;transform:rotate(45deg)}
.card-left .icon{right:-4px}
.card-right .icon{left:-4px}
.card-left .copy{position:absolute;left:56px;top:26px;width:256px}
.card-right .copy{position:absolute;left:162px;top:26px;width:280px}
.card h3{font-size:18px;line-height:18px;font-weight:700;margin-bottom:12px}
.card p{font-size:12.5px;line-height:16.5px;color:var(--body)}
.icon svg{width:50px;height:50px}

/* alternative uses */
.alt-art{left:244px;top:2890px;width:268px;height:402px;background:linear-gradient(170deg,#e2f8f9,#9fe1e5 50%,var(--teal));clip-path:polygon(0 10%,55% 0,100% 30%,100% 60%,55% 100%,0 95%)}
.alt-title{left:532px;top:2950px;font-size:46px;line-height:55px;color:var(--teal);font-weight:700}
.alt-title .accent{color:var(--orange)}
.alt-text{left:536px;top:3076px;width:440px;font-size:14.5px;line-height:21.5px;color:var(--body)}

/* why section */
.why2-title{left:0;top:3462px;width:1200px;text-align:center;font-size:44px;color:var(--white);font-weight:700}
.ticks{position:absolute;list-style:none;color:var(--white);font-size:14px;line-height:18px}
.ticks li{position:relative;padding-left:30px;margin-bottom:22px}
.ticks li svg{position:absolute;left:0;top:0;width:18px;height:18px}
.ticks-left{left:244px;top:3560px;width:350px}
.ticks-right{left:646px;top:3556px;width:330px}

/* footer */
.site-footer .brand{left:513px;top:3917px}
.copyright{left:0;top:3990px;width:1200px;text-align:center;font-size:18px;color:var(--ink)}
</style>
</head>
<body>

<svg class="abs waves" viewBox="0 0 1200 4057" aria-hidden="true">
  <path d="M0 600 C200 560 420 590 640 640 C860 690 1040 640 1200 650 L1200 700 L0 700Z" fill="#e5f6f7"/>
  <path d="M0 680 C180 705 350 690 560 660 C760 632 980 650 1200 665 L1200 1700 C1050 1725 900 1735 720 1712 C500 1684 300 1680 0 1705Z" fill="var(--teal)"/>
  <path d="M0 1705 C300 1680 500 1684 720 1712 C900 1735 1050 1725 1200 1700 L1200 2820 C1000 2850 850 2870 650 2845 C420 2818 220 2815 0 2830Z" fill="var(--grey-bg)"/>
  <path d="M0 3390 C300 3370 700 3355 1200 3330 L1200 3880 C800 3840 400 3875 0 3850Z" fill="#ffd3c6"/>
  <path d="M0 3410 C320 3392 720 3368 1200 3348 L1200 3865 C820 3825 420 3860 0 3830Z" fill="var(--orange)"/>
</svg>

<header class="site-header">
  <div class="abs brand"><span class="brand-dot"></span>Brisk Trail</div>
  <nav class="main-nav">
    <a style="left:348px">Free-Trial</a>
    <a style="left:460px">Contact Us</a>
    <a style="left:572px">Reviews</a>
    <a style="left:668px">Support</a>
    <a style="left:762px">FAQs</a>
    <a style="left:836px">Blog</a>
    <a style="left:904px">Pricing</a>
  </nav>
  <a class="abs btn btn-login">Login</a>
</header>

<section class="hero">
  <h1 class="abs hero-title">Find that document<br><span class="dark">or</span> <span class="accent">item instantly.</span></h1>
  <p class="abs hero-text">Brisk-Trail is a system that allows you to quickly search for the location of every item that you store or file. It is an essential tool for keeping track of paper documents or any other kind of physical item.</p>
  <a class="abs btn btn-more">Read more</a>
  <div class="abs art hero-art" role="img" aria-label="Isometric illustration of a businessman pulling a folder from a filing drawer on a teal laptop"></div>
</section>

<section class="why-storage">
  <h2 class="abs why-title">Why use a storage management<br>system like Brisk-Trail?</h2>
  <h3 class="abs paper-title">Managing paper<br>Documents</h3>
  <div class="abs paper-text">
    <p>Most people and businesses have a variety of documents that need to be filed. The problem is how to do it efficiently so that anything you need can easily be found, even well into the future. Normally, you'd put them in folders on file drawers, sorted in some sort of fashion. But which standard is correct for all kinds of documents? There is no set criterion for every kind of document, so you need to use a combination of them.</p>
    <p>As time passes, you might have a difficult time recalling what criterion you used to file your documents, making it hard to find that document with ease. You might not even find it at all. It becomes even more complex when the person doing the searching isn't the same one as who filed it years ago.</p>
    <p>It is estimated that workers spend over 20% of their time managing documents. A storage management system like Brisk-Trail allows any authorized user to instantly find any document regardless of who filed it or which criterion was used, as long as it was properly filed using the system.</p>
  </div>
  <div class="abs art phone-art" role="img" aria-label="Illustration of a smartphone holding folders with a wine bottle, key, book and test tubes"></div>
</section>

<section class="objects">
  <h2 class="abs objects-title">Managing any non-document objects</h2>
  <p class="abs objects-sub">The same is true of storing any other kind of objects. Common examples include:</p>

  <article class="card card-left" style="left:131px;top:1929px">
    <div class="copy"><h3>Storage boxes, closets, warehouses, and shelves</h3><p>Anything that you put away in storage, would better be indexed with a system that lets you find what you're looking for instantly....</p></div>
    <span class="ring"></span>
    <div class="icon"><svg viewBox="0 0 24 24"><path d="M12 2 21 7v10l-9 5-9-5V7z" fill="var(--orange)"/><path d="M3 7l9 5 9-5M12 12v10" stroke="#fff" stroke-width="1.2" fill="none"/></svg></div>
  </article>
  <article class="card card-right" style="left:606px;top:1922px">
    <span class="ring"></span>
    <div class="icon"><svg viewBox="0 0 24 24"><path d="M2 5c4-1 7 0 10 2v13c-3-2-6-3-10-2zM22 5c-4-1-7 0-10 2v13c3-2 6-3 10-2z" fill="none" stroke="var(--orange)" stroke-width="2" stroke-linejoin="round"/></svg></div>
    <div class="copy"><h3>Books</h3><p>Whether you keep your books on display on shelves, or stored in boxes, you should keep them indexed if you ever want to find any of them in the future.</p></div>
  </article>

  <article class="card card-left" style="left:131px;top:2126px">
    <div class="copy"><h3>Wines</h3><p>Maintaining a constant temperature is essential for good care of quality wines. If you are a wine enthusiast, and have even a small wine cellar fridge, keeping your ....</p></div>
    <span class="ring"></span>
    <div class="icon"><svg viewBox="0 0 24 24"><path d="M7 2h10c0 6-2 9-5 9s-5-3-5-9zM12 11v9M8 21h8" fill="none" stroke="var(--orange)" stroke-width="2" stroke-linecap="round"/><path d="M7.5 6h9c-.5 3-2 4.5-4.5 4.5S8 9 7.5 6z" fill="var(--orange)"/></svg></div>
  </article>
  <article class="card card-right" style="left:606px;top:2119px">
    <span class="ring"></span>
    <div class="icon"><svg viewBox="0 0 24 24"><path d="M12 2 20 5v6c0 5-3.5 9-8 11-4.5-2-8-6-8-11V5z" fill="var(--orange)"/><circle cx="12" cy="11.5" r="4" fill="none" stroke="#fff" stroke-width="1.4"/><path d="M10.3 11.6l1.2 1.2 2.3-2.4" fill="none" stroke="#fff" stroke-width="1.4"/></svg></div>
    <div class="copy"><h3>Safety boxes</h3><p>It is common for people to forget exactly which valuables they have stored in their safety boxes or bank safety deposit boxes</p></div>
  </article>

  <article class="card card-left" style="left:131px;top:2315px">
    <div class="copy"><h3>Moving boxes</h3><p>It is always a good idea to record in detail the contents of each box when you move. Since Brisk-Trail works well on any modern smartphone</p></div>
    <span class="ring"></span>
    <div class="icon"><svg viewBox="0 0 24 24"><g fill="var(--orange)"><rect x="7" y="2" width="10" height="9"/><rect x="2" y="13" width="9" height="9"/><rect x="13" y="13" width="9" height="9"/></g><g stroke="#fff" stroke-width="1.4"><path d="M11 2v3M5 13v3M17 13v3"/></g></svg></div>
  </article>
  <article class="card card-right" style="left:606px;top:2308px">
    <span class="ring"></span>
    <div class="icon"><svg viewBox="0 0 24 24"><path d="M5 2h10l5 5v15H5z" fill="var(--orange)"/><path d="M9 11h7M9 14h7M9 17h7" stroke="#fff" stroke-width="1.4"/><circle cx="7.6" cy="11" r=".7" fill="#fff"/><circle cx="7.6" cy="14" r=".7" fill="#fff"/><circle cx="7.6" cy="17" r=".7" fill="#fff"/></svg></div>
    <div class="copy"><h3>Test samples</h3><p>Laboratory samples frequently need to be stored at constant cold temperatures. Our system was originally designed to fulfill the needs of a laboratory which needs an efficient way</p></div>
  </article>

  <article class="card card-left" style="left:131px;top:2509px">
    <div class="copy"><h3>Audio, video, data, and removable media:</h3><p>Keeping track of the content and storage location of removable media can be a hassle. A system like ours can really help to make that task a breeze.</p></div>
    <span class="ring"></span>
    <div class="icon"><svg viewBox="0 0 24 24"><rect x="4" y="3" width="16" height="18" fill="none" stroke="var(--orange)" stroke-width="2"/><path d="M10 7v6l5-3z" fill="var(--orange)"/><path d="M4 16h16M7 19h3M13 19h4" stroke="var(--orange)" stroke-width="1.6"/></svg></div>
  </article>
  <article class="card card-right" style="left:606px;top:2502px">
    <span class="ring"></span>
    <div class="icon"><svg viewBox="0 0 24 24"><circle cx="16" cy="8" r="5.5" fill="var(--orange)"/><circle cx="17.5" cy="6.5" r="1.5" fill="#fff"/><path d="M12 12 3 21l2 1 1-2 2 1 1-2 2 1 3-5" fill="var(--orange)"/></svg></div>
    <div class="copy"><h3>Keys</h3><p>In a situation such a property management, you can keep track of hundreds of keys for every property you manage. Using Brisk-Trail will easily organize....</p></div>
  </article>
</section>

<section class="alt-uses">
  <div class="abs art alt-art" role="img" aria-label="Illustration of a businessman holding a pencil beside a smartphone with an open drawer"></div>
  <h2 class="abs alt-title">Alternative uses<br>for <span class="accent">Brisk-Trail</span></h2>
  <p class="abs alt-text">How many times have you gone to a restaurant and couldn't recall how good (or bad) each of the dishes were that you previously ordered? You can use Brisk-Trail to record each one to improve your experience for every visit. Our app can also help you decide where you want to go or which dish to recommend when you have a special occasion.</p>
</section>

<section class="why-us">
  <h2 class="abs why2-title">Why Brisk-Trail?</h2>
  <ul class="ticks ticks-left">
    <li><svg viewBox="0 0 24 24"><path d="M3 13l6 6L21 5" fill="none" stroke="#fff" stroke-width="3"/></svg>It is extremely easy to use.</li>
    <li><svg viewBox="0 0 24 24"><path d="M3 13l6 6L21 5" fill="none" stroke="#fff" stroke-width="3"/></svg>It Adapts to your stile. Since each catalog can have 1 or more levels of depth (folders and sub-folders), Brisk-Trail does not force you to use a specific filing or storage methodology.</li>
  </ul>
  <ul class="ticks ticks-right">
    <li><svg viewBox="0 0 24 24"><path d="M3 13l6 6L21 5" fill="none" stroke="#fff" stroke-width="3"/></svg>It's very affordable. Checkout our pricing plans!</li>
    <li><svg viewBox="0 0 24 24"><path d="M3 13l6 6L21 5" fill="none" stroke="#fff" stroke-width="3"/></svg>Since it is online, your data is available almost anywhere in the world.</li>
    <li><svg viewBox="0 0 24 24"><path d="M3 13l6 6L21 5" fill="none" stroke="#fff" stroke-width="3"/></svg>Data encryption ensures that your information is always private, safe, and secure.</li>
  </ul>
</section>

<footer class="site-footer">
  <div class="abs brand"><span class="brand-dot"></span>Brisk Trail</div>
  <p class="abs copyright">Copyright © 2021 All Rights Reserved.</p>
</footer>

</body>
</html>
```